Experienced Handyman needs a business card design

Need a business card design for a one-person Handyman business. This will be my second job (part-time) after retiring from a hands-on 30-year career. I'm experienced, a hard worker, friendly, and do quality work. Everybody needs a handman they can rely on! I've worked with wood and home renovations for 20 years on the side. I'm interested in small, quick jobs - not big renovations, or building decks or garages - more like home maintenance, installing sinks, - things like that.
Walter The Fixer LLC
Quick Fixes Done Well
I'm wondering if the P or H could be made out of tools in my logo...?
Target Market(s)
Homeowners - small jobs
Industry/Entity Type
Handyman / Construction
Contact Information for Business Card
Business name & tagline (see description)...email (Walter@WalterTheFixerpro.example)...phone (555) 417-8862
Look and feel

```html
<!DOCTYPE html>
<html lang="en">
<head>
<meta charset="utf-8">
<title>Walter The Fixer LLC – Business Card</title>
<link href="https://fonts.googleapis.com/css2?family=Rajdhani:wght@600;700&family=Roboto+Condensed:ital,wght@1,700&family=Courgette&display=swap" rel="stylesheet">
<style>
  :root {
    --bg: #8a7458;
    --ink: #232323;
    --orange: #f26a21;
    --white: #ffffff;
  }
  html, body { margin: 0; padding: 0; overflow: hidden; }
  body {
    width: 900px; height: 1200px;
    background: var(--bg);
    position: relative;
    font-family: "Rajdhani", sans-serif;
  }
  .card {
    position: absolute; left: 90px;
    width: 722px; height: 423px;
    overflow: hidden;
    box-shadow: 0 6px 18px rgba(0,0,0,.45);
  }
  .card--front { top: 135px; }
  .card--back { top: 638px; }
  .card__shapes { position: absolute; inset: 0; }
  .abs { position: absolute; margin: 0; white-space: nowrap; }

  /* front */
  .brand-mark {
    left: 40px; top: 112px; width: 235px;
    text-align: center; color: var(--orange);
    font-weight: 700; font-size: 40px; line-height: 1;
  }
  .owner-name { right: 34px; top: 34px; color: var(--orange); font-weight: 700; font-size: 32px; }
  .owner-role { right: 34px; top: 69px; color: var(--white); font-weight: 700; font-size: 20px; letter-spacing: .5px; }
  .services { right: 64px; top: 117px; list-style: none; padding: 0; text-align: right; }
  .services li { color: var(--ink); font-weight: 700; font-size: 22px; line-height: 30px; letter-spacing: .6px; }
  .contact { right: 74px; text-align: right; color: var(--ink); font-weight: 700; }
  .contact--phone { top: 242px; font-size: 33px; letter-spacing: .5px; }
  .contact--email { top: 282px; font-size: 20px; font-weight: 600; }
  .contact--address { top: 312px; font-size: 20px; font-weight: 600; }
  .icon { position: absolute; width: 24px; height: 24px; }
  .bullet { position: absolute; width: 17px; height: 17px; }
  .reg { left: 150px; top: 369px; font-size: 14px; font-weight: 600; color: var(--orange); letter-spacing: .3px; }
  .reg b { color: var(--white); font-weight: 700; }
  .badge-text {
    left: 388px; width: 298px; top: 362px; text-align: center;
    font-family: "Roboto Condensed", sans-serif; font-style: italic; font-weight: 700;
    font-size: 24px; color: var(--ink);
  }

  /* back */
  .mark-square { left: 190px; top: 135px; width: 130px; height: 130px; border: 4px solid var(--white); box-sizing: border-box; }
  .biz-name { left: 382px; top: 140px; color: var(--orange); font-weight: 700; font-size: 60px; line-height: 1; letter-spacing: 1px; }
  .biz-sub { left: 384px; top: 202px; color: var(--white); font-weight: 700; font-size: 24px; letter-spacing: .5px; }
  .biz-tagline { left: 384px; top: 234px; color: var(--orange); font-family: "Courgette", cursive; font-size: 20px; }
  .back-phone { left: 292px; top: 362px; color: var(--white); font-weight: 700; font-size: 27px; letter-spacing: .5px; }
</style>
</head>
<body>

<section class="card card--front">
  <svg class="card__shapes" width="722" height="423" viewBox="0 0 722 423">
    <rect width="722" height="423" fill="#232323"/>
    <polygon points="485,0 722,0 722,423 75,423" fill="#f26a21"/>
    <polygon points="446,40 722,40 722,102 384,102" fill="#232323"/>
    <polygon points="140,355 722,355 722,400 117,400" fill="#232323"/>
    <polygon points="388,379 402,357 672,357 686,379 672,401 402,401" fill="#f26a21"/>
    <polygon points="396,379 406,362 668,362 678,379 668,396 406,396" fill="none" stroke="#232323" stroke-width="2"/>
  </svg>

  <p class="abs brand-mark">WALTER<br>THE FIXER</p>

  <h1 class="abs owner-name">WALTER HALE</h1>
  <p class="abs owner-role">HANDYMAN</p>

  <ul class="abs services">
    <li>HOME MAINTENANCE</li>
    <li>REPAIRS</li>
    <li>INSTALLATIONS</li>
  </ul>
  <svg class="bullet" style="left:669px;top:125px" viewBox="0 0 20 20"><polygon points="5,1 15,1 20,10 15,19 5,19 0,10" fill="#232323"/></svg>
  <svg class="bullet" style="left:669px;top:155px" viewBox="0 0 20 20"><polygon points="5,1 15,1 20,10 15,19 5,19 0,10" fill="#232323"/></svg>
  <svg class="bullet" style="left:669px;top:185px" viewBox="0 0 20 20"><polygon points="5,1 15,1 20,10 15,19 5,19 0,10" fill="#232323"/></svg>

  <p class="abs contact contact--phone">(555) 417-8862</p>
  <p class="abs contact contact--email">walter@walterthefixerpro.example</p>
  <p class="abs contact contact--address">PO Box 4410, Lakeview, WA 99010</p>

  <svg class="icon" style="left:663px;top:251px" viewBox="0 0 24 24" aria-label="phone">
    <polygon points="6,1 18,1 24,12 18,23 6,23 0,12" fill="#232323"/>
    <path d="M8 7c1-1 2-1 2.5 0l1 2c.3.6 0 1-.5 1.4.6 1.3 1.4 2.1 2.6 2.6.4-.5.8-.8 1.4-.5l2 1c1 .5 1 1.5 0 2.5-2.5 2.5-10-5-9-9z" fill="#f26a21"/>
  </svg>
  <svg class="icon" style="left:663px;top:284px" viewBox="0 0 24 24" aria-label="email">
    <polygon points="6,1 18,1 24,12 18,23 6,23 0,12" fill="#232323"/>
    <rect x="6.5" y="8" width="11" height="8" fill="none" stroke="#f26a21" stroke-width="1.6"/>
    <path d="M6.5 8l5.5 4.5L17.5 8" fill="none" stroke="#f26a21" stroke-width="1.6"/>
  </svg>
  <svg class="icon" style="left:663px;top:314px" viewBox="0 0 24 24" aria-label="location">
    <polygon points="6,1 18,1 24,12 18,23 6,23 0,12" fill="#232323"/>
    <path d="M12 18s-4.5-4.5-4.5-7.5a4.5 4.5 0 0 1 9 0C16.5 13.5 12 18 12 18z" fill="none" stroke="#f26a21" stroke-width="1.6"/>
    <circle cx="12" cy="10.5" r="1.6" fill="#f26a21"/>
  </svg>

  <p class="abs reg">CONTRACTOR REG : <b>WALTEFX204KM</b></p>
  <p class="abs badge-text">Quick Fixes Done Well</p>
</section>

<section class="card card--back">
  <svg class="card__shapes" width="722" height="423" viewBox="0 0 722 423">
    <rect width="722" height="423" fill="#232323"/>
    <polygon points="0,0 155,0 0,152" fill="#f26a21"/>
    <polygon points="722,272 722,423 562,423" fill="#f26a21"/>
  </svg>

  <div class="abs mark-square"></div>
  <h2 class="abs biz-name">WALTER</h2>
  <p class="abs biz-sub">THE FIXER LLC</p>
  <p class="abs biz-tagline">Quick Fixes Done Well</p>

  <svg class="icon" style="left:253px;top:367px;width:26px;height:26px" viewBox="0 0 24 24" aria-label="phone">
    <polygon points="6,1 18,1 24,12 18,23 6,23 0,12" fill="#f26a21"/>
    <path d="M8 7c1-1 2-1 2.5 0l1 2c.3.6 0 1-.5 1.4.6 1.3 1.4 2.1 2.6 2.6.4-.5.8-.8 1.4-.5l2 1c1 .5 1 1.5 0 2.5-2.5 2.5-10-5-9-9z" fill="#232323"/>
  </svg>
  <p class="abs back-phone">(555) 417-8862</p>
</section>

</body>
</html>
```